Customizable Gift Note Card Design

I need a gift note card designed for my Healthy Snacks Care Package company. I need to be able to customize each card with the customer's gift message to the recipient and print to a standard printer.

The card should be single-sided 5 x 7, include our logo, keep colors and graphics simple since they will be printed for each individual order on a standard printer. I would like the following quote to be included in a small and subtle way: "Food is symbolic of love when words are inadequate." —Brent K. Hollister. Our website themerrypantrybites.com should also be included.

I have included pictures of our product packaging for reference.

Target Market(s)

Gift recipients: Students, people recovering from illness, housewarming, thank you gifts...etc.

Industry/Entity Type

It Company

Colors

Designer to choose colors to be used in the design.

Requirements
Must have
• We are looking for a simple, cute and elegant gift card that reflects our branding. Must be customizable and printable on a standard printer.
• Must be single-sided 5x7.

```html
<!DOCTYPE html>
<html lang="en">
<head>
<meta charset="utf-8">
<title>The Merry Pantry – Gift Note Card</title>
<link rel="stylesheet" href="https://fonts.googleapis.com/css2?family=Source+Sans+3:wght@400;600;700&display=swap">
<style>
  :root {
    --backdrop: #e6d8c2;
    --kraft: #d8c2a0;
    --kraft-deep: #cdb48e;
    --crimson: #8c0a14;
    --crimson-bright: #b0121f;
    --ink: #111111;
    --paper: #ffffff;
    --muted: #5a4a3a;
  }
  * { margin: 0; padding: 0; box-sizing: border-box; }
  html, body {
    width: 1200px;
    height: 916px;
    overflow: hidden;
    background: var(--backdrop);
    font-family: "Source Sans 3", Arial, sans-serif;
  }
  .note-card {
    position: absolute;
    left: 300px;
    top: 38px;
    width: 600px;
    height: 840px;
    background: var(--paper);
    overflow: hidden;
    box-shadow: 0 6px 24px rgba(80, 60, 30, 0.18);
  }
  .card-shapes {
    position: absolute;
    inset: 0;
    width: 600px;
    height: 840px;
  }
  .mascot-area {
    position: absolute;
    left: 385px;
    top: 30px;
    width: 165px;
    height: 270px;
    border-radius: 6px;
    background: linear-gradient(180deg, rgba(17,17,17,0.28), rgba(140,10,20,0.18) 50%, rgba(17,17,17,0.24));
  }
  .quote {
    position: absolute;
    left: 40px;
    top: 140px;
    width: 330px;
    text-align: right;
    color: var(--crimson);
  }
  .quote-text {
    font-weight: 700;
    font-size: 31px;
    line-height: 1.08;
  }
  .quote-author {
    margin-top: 4px;
    padding-right: 110px;
    font-weight: 400;
    font-size: 15px;
    color: var(--muted);
  }
  .web-ribbon {
    position: absolute;
    left: 340px;
    top: 722px;
    width: 260px;
    height: 32px;
    display: flex;
    align-items: center;
    justify-content: flex-end;
    padding-right: 16px;
    color: var(--paper);
    font-weight: 600;
    font-size: 13px;
    letter-spacing: 0.3px;
  }
  .brand {
    position: absolute;
    left: 36px;
    top: 784px;
    display: flex;
    align-items: center;
    gap: 8px;
  }
  .brand-dot {
    width: 22px;
    height: 22px;
    border-radius: 50%;
    background: var(--ink);
  }
  .brand-name {
    font-weight: 700;
    font-size: 18px;
    color: var(--ink);
  }
</style>
</head>
<body>
  <main class="note-card">
    <svg class="card-shapes" viewBox="0 0 600 840" aria-hidden="true">
      <rect class="kraft-panel" x="0" y="0" width="600" height="335" fill="var(--kraft)"/>
      <polygon class="corner-accent-red" points="600,240 600,335 455,335" fill="var(--crimson-bright)"/>
      <rect class="band" x="0" y="330" width="600" height="56" fill="var(--crimson)"/>
      <polygon class="corner-accent-black" points="0,386 135,386 0,555" fill="var(--ink)"/>
      <polygon class="ribbon" points="330,722 600,722 600,754 330,754 344,738" fill="var(--crimson)"/>
    </svg>

    <div class="mascot-area" role="img" aria-label="Brand mascot illustration: bowler hat, red glasses, moustache and bow tie"></div>

    <blockquote class="quote">
      <p class="quote-text">"Food is symbolic<br>of love when words<br>are inadequate."</p>
      <p class="quote-author">—Brent K. Hollister</p>
    </blockquote>

    <div class="web-ribbon">www.themerrypantrybites.com/</div>

    <div class="brand">
      <span class="brand-dot"></span>
      <span class="brand-name">The Merry Pantry</span>
    </div>
  </main>
</body>
</html>
```